Professional, elegant brochure for funeral home

We have a funeral home. We would like a 2 sided brochure. On one side will be 3 columns for our cremation options and on the other side would be 2-3 columns of our burial options. Would like to print it and also will be putting it on our website at www.Varnelhaven.com

Use as examples

https://www.brimtolgrace.com/pricing-and-resources/online-cremation-package-options

https://pelladinechapel.com/wp-content/uploads/Cremation-with-Ceremony-Plans.pdf

We only need a simple 1page (front and back brochure). Once we have decided on the designer I can provide the final content to be placed on the brochure.

Target Market(s)

We are family owned business so Something soft, inviting, personable and looks professionally done.

Industry/Entity Type

Funeral Home

Requirements
Must have
• Look professional. Easy to read
Nice to have
• Softer Muted comforting colors. No bright colors.

```html
<!DOCTYPE html>
<html lang="en">
<head>
<meta charset="utf-8">
<title>Varnel Haven Funeral Home – Cremation & Burial Options</title>
<link rel="stylesheet" href="https://fonts.googleapis.com/css2?family=Playfair+Display:wght@700;900&family=Montserrat:wght@400;500;900&family=EB+Garamond:wght@400;500&display=swap">
<style>
  :root{
    --backdrop:#616161;
    --paper:#ffffff;
    --sky:#1192dc;
    --sky-deep:#0a6fb0;
    --leaf:#b4cb3b;
    --leaf-deep:#a2ba2c;
    --cream:#fdf1e2;
    --ink:#222222;
    --ink-soft:#3a3a3a;
    --hero-blue:rgba(22,86,225,.82);
  }
  *{box-sizing:border-box;margin:0;padding:0}
  html,body{width:1200px;height:833px;overflow:hidden}
  body{background:var(--backdrop);position:relative;font-family:"Montserrat",sans-serif;color:var(--ink)}

  .sheet{position:absolute;top:71px;width:535px;height:692px;background:var(--paper)}
  .sheet--cremation{left:50px;--band:var(--sky);--head:var(--leaf);--price-a:var(--sky-deep);--price-b:var(--sky);--foot:var(--leaf);--accent:var(--sky)}
  .sheet--burial{left:614px;--band:var(--leaf);--head:var(--sky);--price-a:var(--leaf-deep);--price-b:var(--leaf);--foot:var(--sky);--accent:var(--sky)}

  .hero{position:absolute;left:16px;top:16px;width:503px;height:215px;overflow:hidden}
  .hero-photo{position:absolute;inset:0}
  .sheet--cremation .hero-photo{background:linear-gradient(90deg,#4c4f50 0%,#6e7170 38%,#8c6d74 58%,#d97a9c 75%,#f3a3bd 88%,#7f9b55 100%)}
  .sheet--burial .hero-photo{background:linear-gradient(180deg,#dfe7ee 0%,#c7d2e0 20%,#9a84c9 40%,#7b58be 62%,#6c7f3c 85%,#5f8a34 100%)}

  .brand{position:absolute;left:37px;top:54px;color:#fff;font-family:"Playfair Display",serif;font-weight:700;font-size:19px;line-height:1.15;letter-spacing:1px}
  .brand-tagline{position:absolute;left:40px;top:107px;color:#e8e8e8;font-family:"EB Garamond",serif;font-size:13px}

  .hero-word{position:absolute;font-family:"Montserrat",sans-serif;font-weight:900;color:var(--hero-blue);line-height:1}
  .hero-word--ahead{left:30px;top:136px;font-size:74px;letter-spacing:-3px}
  .hero-word--life{left:118px;top:97px;font-size:118px;letter-spacing:-4px}
  .hero-kicker{position:absolute;color:#fff;font-family:"Playfair Display",serif;font-weight:700;white-space:nowrap}
  .hero-kicker--plan{left:96px;top:156px;font-size:13px;letter-spacing:3px}
  .hero-kicker--celebrate{left:155px;top:150px;font-size:20px;letter-spacing:10px}

  .band{position:absolute;left:16px;top:231px;width:503px;height:39px;background:var(--band);color:#fff;font-family:"Playfair Display",serif;font-weight:700;font-size:24px;letter-spacing:8px;text-align:center;line-height:40px}

  .popular{position:absolute;left:0;width:535px;top:277px;text-align:center;color:var(--accent);font-family:"Playfair Display",serif;font-weight:700;font-size:9px;line-height:1.15}

  .plan{position:absolute}
  .plan--basic{left:23px;width:153px}
  .plan--featured{left:181px;width:174px}
  .plan--premier{left:359px;width:153px}
  .plan-body{position:absolute;left:0;right:0;background:var(--cream)}
  .plan--basic .plan-body,.plan--premier .plan-body{top:340px;height:179px;left:6px;right:6px}
  .plan--featured .plan-body{top:340px;height:187px;left:6px;right:6px}
  .plan-head{position:absolute;left:0;right:0;background:var(--head);color:#fff;font-family:"Playfair Display",serif;font-weight:700;text-align:center;font-size:14px;line-height:1.2;letter-spacing:.5px}
  .plan--basic .plan-head,.plan--premier .plan-head{top:316px;height:53px;padding-top:8px;clip-path:polygon(0 0,100% 0,100% 72%,50% 100%,0 72%)}
  .plan--featured .plan-head{top:304px;height:51px;padding-top:9px;clip-path:polygon(0 0,100% 0,100% 86%,50% 100%,0 86%)}
  .plan-list{position:absolute;list-style:none;left:10px;right:6px;top:378px}
  .plan--featured .plan-list{left:17px}
  .plan-list li{position:relative;padding-left:11px;font-size:8.6px;line-height:11.5px;height:26.8px;color:var(--ink)}
  .plan--featured .plan-list li{height:27.7px}
  .plan-list li svg{position:absolute;left:0;top:2px;width:7px;height:7px}
  .plan-price{position:absolute;left:0;right:0;background:linear-gradient(180deg,var(--price-a),var(--price-b));color:#fff;font-family:"Playfair Display",serif;font-weight:900;font-size:21px;text-align:center}
  .plan--basic .plan-price{top:519px;height:34px;line-height:34px}
  .plan--premier .plan-price{top:518px;height:34px;line-height:34px}
  .plan--featured .plan-price{top:527px;height:36px;line-height:36px}

  .bouquet{position:absolute;left:375px;top:548px;width:120px;height:100px;border-radius:50% 50% 40% 40%;background:radial-gradient(circle at 55% 35%,#e46a9a 0%,#c8608a 25%,#7fa845 55%,rgba(255,255,255,0) 75%)}

  .ceremony{position:absolute;left:32px;top:572px;width:300px}
  .ceremony h2{font-family:"EB Garamond",serif;font-weight:500;font-size:16px;letter-spacing:.3px;color:#111}
  .ceremony p{margin-top:6px;font-family:"EB Garamond",serif;font-size:7.6px;line-height:10px;color:var(--ink-soft)}

  .footer{position:absolute;left:16px;top:641px;width:503px;height:34px;background:var(--foot);color:#fff;display:flex;align-items:center;justify-content:center;gap:22px;font-size:11.5px}
  .contact{display:flex;align-items:center;gap:4px}
  .contact svg{width:9px;height:9px}
  .divider{opacity:.9}
  .social-dot{width:14px;height:14px;border-radius:50%;background:#fff}
</style>
</head>
<body>

<svg width="0" height="0" style="position:absolute">
  <defs>
    <symbol id="tick" viewBox="0 0 10 10"><path d="M1 5.5 L4 8.5 L9 1.5" fill="none" stroke="#333" stroke-width="1.3"/></symbol>
    <symbol id="globe" viewBox="0 0 10 10"><g fill="none" stroke="#fff" stroke-width=".9"><circle cx="5" cy="5" r="4.3"/><ellipse cx="5" cy="5" rx="1.8" ry="4.3"/><path d="M.7 5h8.6"/></g></symbol>
    <symbol id="phone" viewBox="0 0 10 10"><circle cx="5" cy="5" r="4.3" fill="none" stroke="#fff" stroke-width=".9"/><path d="M3.5 2.8c.3-.3.6 0 .8.4s.2.6-.1.8c.2.6.8 1.3 1.3 1.5.2-.3.5-.3.8-.1s.6.5.3.8c-.4.5-1.1.5-1.9-.1-.8-.6-1.5-1.6-1.6-2.3 0-.5.2-.8.4-1z" fill="#fff"/></symbol>
  </defs>
</svg>

<!-- Cremation side -->
<article class="sheet sheet--cremation">
  <div class="hero">
    <div class="hero-photo" role="img" aria-label="Photo of pink blossoms on a branch against a soft grey background"></div>
    <div class="brand">Varnel Haven<br>Funeral Home</div>
    <div class="brand-tagline">Cremation · Burial · Pre-Planning</div>
    <div class="hero-word hero-word--ahead">AHEAD</div>
    <div class="hero-kicker hero-kicker--plan">LIVE WELL, PLAN</div>
  </div>
  <div class="band">CREMATION OPTIONS</div>
  <div class="popular">MOST<br>POPULAR</div>

  <section class="plan plan--basic">
    <div class="plan-body"></div>
    <h3 class="plan-head">BASIC<br>CREMATION</h3>
    <ul class="plan-list">
      <li><svg><use href="#tick"/></svg>Lorem ipsum dolor sit amet, consectetur</li>
      <li><svg><use href="#tick"/></svg>Lorem ipsum dolor sit amet, consectetur</li>
      <li><svg><use href="#tick"/></svg>Lorem ipsum dolor sit amet, consectetur</li>
      <li><svg><use href="#tick"/></svg>Lorem ipsum dolor sit amet, consectetur</li>
      <li><svg><use href="#tick"/></svg>Lorem ipsum dolor sit amet, consectetur</li>
    </ul>
    <div class="plan-price">$1.099.00</div>
  </section>
  <section class="plan plan--featured">
    <div class="plan-body"></div>
    <h3 class="plan-head">CREMATION WITH<br>CONFIDENCE</h3>
    <ul class="plan-list">
      <li><svg><use href="#tick"/></svg>Lorem ipsum dolor sit amet, consectetur</li>
      <li><svg><use href="#tick"/></svg>Lorem ipsum dolor sit amet, consectetur</li>
      <li><svg><use href="#tick"/></svg>Lorem ipsum dolor sit amet, consectetur</li>
      <li><svg><use href="#tick"/></svg>Lorem ipsum dolor sit amet, consectetur</li>
      <li><svg><use href="#tick"/></svg>Lorem ipsum dolor sit amet, consectetur</li>
    </ul>
    <div class="plan-price">$1.799.00</div>
  </section>
  <section class="plan plan--premier">
    <div class="plan-body"></div>
    <h3 class="plan-head">PREMIER<br>CREMATION</h3>
    <ul class="plan-list">
      <li><svg><use href="#tick"/></svg>Lorem ipsum dolor sit amet, consectetur</li>
      <li><svg><use href="#tick"/></svg>Lorem ipsum dolor sit amet, consectetur</li>
      <li><svg><use href="#tick"/></svg>Lorem ipsum dolor sit amet, consectetur</li>
      <li><svg><use href="#tick"/></svg>Lorem ipsum dolor sit amet, consectetur</li>
      <li><svg><use href="#tick"/></svg>Lorem ipsum dolor sit amet, consectetur</li>
    </ul>
    <div class="plan-price">$2.499.00</div>
  </section>

  <div class="bouquet" role="img" aria-label="Bouquet of pink tulips with white blossoms"></div>
  <div class="ceremony">
    <h2>The Importance of Ceremony</h2>
    <p>Meaningful ceremonies and rituals create a transformative life experience. Reflecting and remembering a person's legacy in the presence of gathered community...this is when healing begins.</p>
  </div>

  <footer class="footer">
    <span class="contact"><svg><use href="#globe"/></svg>www.varnelhavenfh.com</span>
    <span class="contact"><svg><use href="#phone"/></svg>(555) 214-3180</span>
    <span class="contact"><svg><use href="#phone"/></svg>(555) 306-7742</span>
    <span class="divider">|</span>
    <span class="social-dot"></span>
  </footer>
</article>

<!-- Burial side -->
<article class="sheet sheet--burial">
  <div class="hero">
    <div class="hero-photo" role="img" aria-label="Photo of a lavender field under a pale sky"></div>
    <div class="hero-word hero-word--life">LIFE</div>
    <div class="hero-kicker hero-kicker--celebrate">CELEBRATE</div>
  </div>
  <div class="band">BURIAL OPTIONS</div>
  <div class="popular">MOST<br>POPULAR</div>

  <section class="plan plan--basic">
    <div class="plan-body"></div>
    <h3 class="plan-head">BASIC<br>BURIAL</h3>
    <ul class="plan-list">
      <li><svg><use href="#tick"/></svg>Lorem ipsum dolor sit amet, consectetur</li>
      <li><svg><use href="#tick"/></svg>Lorem ipsum dolor sit amet, consectetur</li>
      <li><svg><use href="#tick"/></svg>Lorem ipsum dolor sit amet, consectetur</li>
      <li><svg><use href="#tick"/></svg>Lorem ipsum dolor sit amet, consectetur</li>
      <li><svg><use href="#tick"/></svg>Lorem ipsum dolor sit amet, consectetur</li>
    </ul>
    <div class="plan-price">$1.099.00</div>
  </section>
  <section class="plan plan--featured">
    <div class="plan-body"></div>
    <h3 class="plan-head">BURIAL WITH<br>CONFIDENCE</h3>
    <ul class="plan-list">
      <li><svg><use href="#tick"/></svg>Lorem ipsum dolor sit amet, consectetur</li>
      <li><svg><use href="#tick"/></svg>Lorem ipsum dolor sit amet, consectetur</li>
      <li><svg><use href="#tick"/></svg>Lorem ipsum dolor sit amet, consectetur</li>
      <li><svg><use href="#tick"/></svg>Lorem ipsum dolor sit amet, consectetur</li>
      <li><svg><use href="#tick"/></svg>Lorem ipsum dolor sit amet, consectetur</li>
    </ul>
    <div class="plan-price">$1.799.00</div>
  </section>
  <section class="plan plan--premier">
    <div class="plan-body"></div>
    <h3 class="plan-head">PREMIER<br>BURIAL</h3>
    <ul class="plan-list">
      <li><svg><use href="#tick"/></svg>Lorem ipsum dolor sit amet, consectetur</li>
      <li><svg><use href="#tick"/></svg>Lorem ipsum dolor sit amet, consectetur</li>
      <li><svg><use href="#tick"/></svg>Lorem ipsum dolor sit amet, consectetur</li>
      <li><svg><use href="#tick"/></svg>Lorem ipsum dolor sit amet, consectetur</li>
      <li><svg><use href="#tick"/></svg>Lorem ipsum dolor sit amet, consectetur</li>
    </ul>
    <div class="plan-price">$2.499.00</div>
  </section>

  <div class="bouquet" role="img" aria-label="Bouquet of pink tulips with white blossoms"></div>
  <div class="ceremony">
    <h2>The Importance of Ceremony</h2>
    <p>Meaningful ceremonies and rituals create a transformative life experience. Reflecting and remembering a person's legacy in the presence of gathered community...this is when healing begins.</p>
  </div>

  <footer class="footer">
    <span class="contact"><svg><use href="#globe"/></svg>www.varnelhavenfh.com</span>
    <span class="contact"><svg><use href="#phone"/></svg>(555) 214-3180</span>
    <span class="contact"><svg><use href="#phone"/></svg>(555) 306-7742</span>
    <span class="divider">|</span>
    <span class="social-dot"></span>
  </footer>
</article>

</body>
</html>
```